Halvorsen Construction Needs a Business Card

Our current business card is very bland, and since we have a new logo, we would like a new business card design to reflect our company. It can be a single-sided or two-sided card, but it is important that our contact information appears on the same side. I am attaching a copy of our old card and our new logo. If you need the logo in another format than the one I'm sending, please let me know. This is the information that we must have on our card, but not necessarily in any specific order:
1) Our logo
2) General Contractor
3) Dale Halvorsen, Owner
4) 482 Commerce Ridge Road, Pine Hollow, Georgia 35871
5) Office: 555-555-0147
7) Fax: 555-555-0148
8) Cell: 555-555-0193
9) halvorsenconstruction@qvl-mail.net
10) halvorsenconstruction-example.com (can be omitted if necessary)
Also, I will need files in a format that I can alter if any of the above information changes in the near future. Thank you in advance for your submissions!
Target Market(s)
Commercial and residential clients, architects, and subcontractors.
Industry/Entity Type
Business
Look and feel

```html
<!DOCTYPE html>
<html lang="en">
<head>
<meta charset="utf-8">
<title>Halvorsen Construction – Business Card</title>
<link rel="stylesheet" href="https://fonts.googleapis.com/css2?family=Archivo:wght@400;700;800&display=swap">
<style>
  :root {
    --bg: #e7e6e4;
    --card: #ffffff;
    --ink: #1d1d1b;
    --muted: #3a3a38;
    --accent: #f6b91c;
    --shadow: rgba(0,0,0,0.18);
  }
  * { box-sizing: border-box; margin: 0; padding: 0; }
  html, body { width: 1200px; height: 716px; overflow: hidden; }
  body {
    background: var(--bg);
    font-family: "Archivo", Arial, sans-serif;
    color: var(--ink);
    position: relative;
  }
  .card {
    position: absolute;
    top: 209px;
    width: 520px;
    height: 297px;
    background: var(--card);
    border-radius: 6px;
    box-shadow: 0 10px 28px var(--shadow);
    overflow: hidden;
  }
  .card--front { left: 50px; }
  .card--back { left: 630px; }

  .brand {
    display: flex;
    align-items: center;
    gap: 14px;
  }
  .brand__square {
    width: 46px;
    height: 46px;
    background: var(--ink);
    flex: none;
  }
  .brand__name {
    font-weight: 800;
    font-size: 30px;
    line-height: 1;
    letter-spacing: -0.5px;
    text-transform: uppercase;
    color: var(--ink);
  }

  .card--front .brand {
    position: absolute;
    left: 50%;
    top: 50%;
    transform: translate(-50%, -50%);
  }

  .card--back .brand { position: absolute; left: 36px; top: 34px; }
  .card--back .brand__square { width: 40px; height: 40px; }
  .card--back .brand__name { font-size: 26px; white-space: nowrap; }

  .tagline {
    position: absolute;
    left: 90px;
    top: 82px;
    font-size: 15px;
    letter-spacing: 3.4px;
    text-transform: uppercase;
    color: var(--muted);
  }

  .contact {
    position: absolute;
    left: 36px;
    top: 128px;
    width: 430px;
    font-size: 12.5px;
    color: var(--muted);
  }
  .contact__person { margin-bottom: 10px; }
  .contact__name { font-weight: 800; font-size: 17px; color: var(--ink); }
  .contact__role { font-size: 13px; margin-left: 6px; text-transform: uppercase; }
  .contact__row {
    padding: 6px 0 5px;
    white-space: nowrap;
  }
  .contact__row--ruled { border-bottom: 2px solid var(--accent); }
  .label { font-weight: 700; color: var(--accent); text-transform: uppercase; margin-right: 3px; }
  .label--gap { margin-left: 10px; }
</style>
</head>
<body>
  <section class="card card--front" aria-label="Card front">
    <div class="brand">
      <span class="brand__square"></span>
      <span class="brand__name">Halvorsen Construction</span>
    </div>
  </section>

  <section class="card card--back" aria-label="Card back">
    <div class="brand">
      <span class="brand__square"></span>
      <span class="brand__name">Halvorsen Construction</span>
    </div>
    <p class="tagline">General Contractor</p>

    <div class="contact">
      <p class="contact__person">
        <span class="contact__name">Dale Halvorsen</span><span class="contact__role">Owner</span>
      </p>
      <p class="contact__row">
        <span class="label">Phone</span>555-555-0147
        <span class="label label--gap">Fax</span>555-555-0148
      </p>
      <p class="contact__row contact__row--ruled">
        <span class="label">Cell</span>555-555-0193
        <span class="label label--gap">Email</span>halvorsenconstruction@qvl-mail.net
      </p>
      <p class="contact__row contact__row--ruled">482 Commerce Ridge Road, Pine Hollow, Georgia 35871</p>
    </div>
  </section>
</body>
</html>
```